Web design for online activity booking website

Our activity booking website uTrundle.net is looking outdated and needing a loving revamp on its design and STRUCTURE. it was initially created as a destination guide before we modified the homepage slightly to sell activities. So please DON'T RELY on the current website for your design. Now, the focus is ACTIVITY, while guide/ info should come only as secondary.

In other words, we will be doing something very similar to Wandelo.com (a bit crowded for our liking) and FindMyOuting.com. If you could capture the best essences of both, that would be awesome! Besides, we also like roostly.com's simplicity.

SIMPLE, CLEAN, BRIGHT, USER and MOBILE FRIENDLY please :)

We have a new logo created and some wireframes (a few more in progress) so you know the basic components required in each page. These are just rough ideas so please ignore the ratio/size, colours etc and if you have a better way of arranging or simplifying things, please do so :)

Help us make it a website that everyone would love!

Thank you in advance for your time and artistry.

Target Market(s)

Internet savvy travellers between 18-65

Industry/Entity Type

Tourism

Number of Pages Required

5+ page

Requirements
Must have
• SIMPLE, CLEAN feel, USER and MOBILE FRIENDLY please :)
• See attachments for rough structure. Will also need standard pages such as:
• - About Us
• - Contact Us
• - Wishlist etc
• Message from our developer "designer to keep layers in PSD format accurately so html/css code does not need to lead a mess in photoshop"
Nice to have
• UPDATE: We are so thrilled to receive so many web designs but on the other hand, the submissions are getting too generic and everyone's designs is almost looking identical (many look like they are “borrowed” from existing popular websites). This is making the selection and decision process very difficult.
• So instead of sending us more of the very similar homepage design with minor tweaks (which we can do during handover section anyway), please send us a design of more specific page of our website. Please refer job brief, file no. 5 - Product detail page.
• This will give us better idea of your skills and choose the best as winner to work on the rest of our web pages.
Should not have
• No dark background please

```html
<!DOCTYPE html>
<html lang="en">
<head>
<meta charset="utf-8">
<title>uTrundle – Book Activities</title>
<link href="https://fonts.googleapis.com/css2?family=Marcellus&family=Montserrat:wght@400;500;600;700&display=swap" rel="stylesheet">
<style>
:root{
  --teal:#16b5b3;
  --teal-dark:#0f9e9c;
  --ink:#1c1c1c;
  --muted:#555;
  --grey-band:#e7e7e7;
  --footer:#0b0b0b;
  --white:#ffffff;
  --serif:"Marcellus", Georgia, serif;
  --sans:"Montserrat", Arial, sans-serif;
}
*{box-sizing:border-box;margin:0;padding:0}
html,body{width:1200px;height:3622px;overflow:hidden}
body{position:relative;font-family:var(--sans);color:var(--ink);background:var(--white)}
section,header,footer{position:absolute;left:0;width:1200px}
.abs{position:absolute}

/* hero */
.hero{top:0;height:657px;background:linear-gradient(180deg,#3f7fc9 0%,#7fb2dd 22%,#6f8a6e 40%,#3f6a2a 58%,#2c2a24 80%,#3a3530 100%)}
.util{top:29px;left:77px;display:flex;gap:8px}
.util span{display:flex;align-items:center;justify-content:space-between;height:34px;padding:0 12px;background:#1d2d3c;color:#fff;font-size:13px;font-weight:500;border-radius:2px}
.util .lang{width:102px}.util .cur{width:102px}
.util .login{width:106px;background:#1b3a52;justify-content:center;gap:8px}
.brand{top:22px;left:0;width:1200px;text-align:center}
.brand .name{font-family:var(--sans);font-weight:700;font-size:50px;color:#fff;line-height:1}
.brand .tag{font-size:9px;letter-spacing:2px;color:#fff;margin-top:6px;font-weight:600}
.toplinks{top:32px;right:77px;display:flex;gap:26px;color:#fff;font-size:16px;align-items:center}
.toplinks span{display:flex;align-items:center;gap:7px}
.nav{top:116px;left:297px;display:flex;height:55px;align-items:center}
.nav a{color:#fff;text-decoration:none;font-size:16px;font-weight:600;padding:0 22px;height:55px;display:flex;align-items:center}
.nav a.on{background:var(--teal)}
.booker{top:266px;left:263px;width:674px;height:258px;background:rgba(30,30,30,.55);border:1px solid rgba(255,255,255,.6);text-align:center;color:#fff}
.booker h1{font-family:var(--serif);font-weight:400;font-size:32px;letter-spacing:1px;margin-top:34px}
.booker p{font-size:19px;font-weight:600;margin-top:4px}
.selects{display:flex;gap:13px;justify-content:center;margin-top:26px}
.selects span{width:292px;height:44px;border:1px solid #fff;display:flex;align-items:center;justify-content:space-between;padding:0 14px;font-size:13px;font-weight:600}
.btn-teal{display:inline-block;background:var(--teal);color:#fff;font-weight:600;font-size:14px;border-radius:2px}
.booker .btn-teal{margin-top:8px;width:125px;height:44px;line-height:44px}
.dots{top:601px;left:567px;display:flex;gap:12px}
.dots i{width:20px;height:20px;background:#111;border:2px solid #888;display:block}
.dots i.on{background:var(--teal)}

/* features */
.features{top:657px;height:111px;background:var(--grey-band);border-top:7px solid var(--teal)}
.feat{position:absolute;top:0;height:104px;display:flex;flex-direction:column;align-items:center;justify-content:center;font-family:var(--serif);font-size:17px;gap:8px}
.feat+.feat{border-left:2px solid #fff}
.feat.lead{align-items:flex-start;font-size:18px;font-weight:700;font-family:var(--sans);gap:2px}
.feat.lead small{font-family:var(--serif);font-weight:400;font-size:17px}

/* headings */
.sec-title{font-family:var(--serif);font-weight:400;color:var(--teal);text-align:center;font-size:46px;letter-spacing:1px;width:1200px}
.sec-sub{text-align:center;font-size:14px;width:1200px;font-weight:500}
.btn-outline{display:flex;align-items:center;justify-content:center;border:2px solid var(--teal);color:var(--ink);font-family:var(--serif);font-size:17px;background:#fff}

/* destinations */
.dest{top:768px;height:792px}
.grid{top:145px;left:77px;width:1046px;display:grid;grid-template-columns:repeat(3,1fr);grid-auto-rows:260px}
.tile{position:relative}
.tile .over{position:absolute;top:22px;left:0;width:100%;text-align:center;color:#fff;font-weight:700;font-size:20px}

/* welcome */
.welcome{top:1560px;height:415px;background:linear-gradient(100deg,#2a2f33 0%,#444a4b 45%,#2f3234 75%,#3d3a33 100%);text-align:center;color:#fff}
.welcome h2{font-family:var(--serif);font-weight:400;font-size:58px;color:#2cd0cc;margin-top:62px}
.welcome p{width:740px;margin:22px auto 0;font-size:17px;font-weight:700;line-height:1.75}
.welcome .get{position:absolute;left:495px;top:289px;width:207px;height:48px;background:#5e5e5e;color:#fff;font-size:15px;font-weight:700;display:flex;align-items:center;justify-content:center}

/* activities */
.acts{top:1975px;height:789px}
.search{top:145px;left:298px;width:604px;height:48px;border:1px solid #bbb;display:flex;align-items:center;justify-content:space-between;padding:0 18px;font-size:14px;font-weight:600;color:#444}
.card{position:absolute;top:227px;width:311px;height:432px;border:1px solid var(--teal);background:#fff}
.card .pic{height:176px}
.card h3{font-family:var(--serif);font-weight:400;font-size:17px;margin:22px 0 0 19px}
.card .price{color:var(--teal);font-weight:700;font-size:14px;margin:16px 0 0 19px}
.card p{font-size:14px;line-height:1.55;margin:12px 19px 0;color:#222}
.card .book{position:absolute;left:18px;top:315px;width:178px;height:52px;display:flex;align-items:center;justify-content:center;font-size:15px;font-weight:600;border:2px solid var(--teal);color:var(--teal)}
.card .book.fill{background:var(--teal);color:#fff}
.card .foot{position:absolute;left:0;bottom:0;width:100%;height:46px;background:var(--teal);display:flex;align-items:center;justify-content:space-between;padding:0 16px;color:#111;font-size:13px;font-weight:600}
.stars{display:flex;gap:4px}

/* recommended */
.recom{top:2764px;height:314px;background:linear-gradient(90deg,#8f8a6e 0%,#d8d6cd 30%,#e6e3dc 55%,#c9c7bf 80%,#b6b2a4 100%)}
.recom h2{position:absolute;top:40px;width:1200px;text-align:center;font-size:18px;font-weight:700}
.strip{top:106px;left:77px;display:flex}
.strip div{width:174.33px;height:155px;position:relative}
.strip .label{position:absolute;top:0;left:0;width:100%;height:100%;display:flex;align-items:center;justify-content:center;color:#fff;font-weight:700;font-size:18px}

/* references */
.refs{top:3078px;height:229px;background:var(--teal);color:#fff}
.refs h2{position:absolute;top:30px;width:1200px;display:flex;justify-content:center;align-items:center;gap:22px;font-size:21px;font-weight:500}
.refs h2::before,.refs h2::after{content:"";width:105px;height:1px;background:#fff}
.ref-col{position:absolute;top:88px;list-style:none;font-size:13px}
.ref-col li{height:26.5px}
.ref-col li::before{content:"»";font-weight:700;margin-right:8px}

/* footer */
.site-foot{top:3307px;height:315px;background:var(--footer);color:#fff}
.fcol{position:absolute;top:38px}
.fcol h4{font-family:var(--serif);font-weight:400;color:var(--teal);font-size:22px;letter-spacing:1px;margin-bottom:14px}
.fcol ul{list-style:none;font-size:13px;font-weight:600;line-height:21px}
.social{top:41px;left:756px;display:flex;gap:10px}
.social i{width:53px;height:53px;background:var(--teal);display:block}
.social i:nth-child(n+2){background:#1e1e1e}
.newsletter{top:121px;left:760px;width:363px;height:55px;border:1px solid #777;display:flex;align-items:center;justify-content:space-between;padding:0 14px;font-size:13px;font-weight:600}
.copy{top:253px;left:77px;width:1046px;border-top:1px solid #333;padding-top:24px;text-align:center;font-size:12px}
.copy b{color:var(--teal);font-weight:600}
</style>
</head>
<body>

<header class="hero" role="img" aria-label="Photo of a volcanic mountain landscape with pine forest under a blue sky">
  <div class="util abs">
    <span class="lang">English <svg width="10" height="6"><path d="M0 0h10L5 6z" fill="#fff"/></svg></span>
    <span class="cur">USD ($) <svg width="10" height="6"><path d="M0 0h10L5 6z" fill="#fff"/></svg></span>
    <span class="login"><svg width="13" height="13" viewBox="0 0 13 13"><circle cx="6.5" cy="4" r="3" fill="#fff"/><path d="M1 13c0-4 11-4 11 0z" fill="#fff"/></svg>Login</span>
  </div>
  <div class="brand abs">
    <div class="name">uTrundle</div>
    <div class="tag">YOUR ADVENTURE STARTS HERE !</div>
  </div>
  <div class="toplinks abs">
    <span><svg width="18" height="16" viewBox="0 0 18 16"><path d="M9 16L1.5 8.5A4.5 4.5 0 019 3a4.5 4.5 0 017.5 5.5z" fill="#fff"/></svg>Wishlist</span>
    <span><svg width="20" height="16" viewBox="0 0 20 16"><path d="M0 1h3l3 10h11l2-7H5" stroke="#fff" stroke-width="2" fill="none"/><circle cx="8" cy="14" r="1.6" fill="#fff"/><circle cx="15" cy="14" r="1.6" fill="#fff"/></svg>Cart</span>
    <span><svg width="18" height="18" viewBox="0 0 18 18"><circle cx="9" cy="9" r="9" fill="#111"/><text x="9" y="13.5" font-size="12" font-weight="700" text-anchor="middle" fill="#fff" font-family="Arial">?</text></svg>Help</span>
  </div>
  <nav class="nav abs">
    <a class="on">HOME</a><a>ABOUT US</a><a>GALLARY</a><a>BLOG</a><a>CONTACT US</a>
  </nav>
  <div class="booker abs">
    <h1>BOOK ACTIVITIES NOW</h1>
    <p>Your Adventure Starts Here</p>
    <div class="selects">
      <span>CHOOSE DESTINATION <svg width="14" height="8"><path d="M1 1l6 6 6-6" stroke="#fff" fill="none" stroke-width="1.5"/></svg></span>
      <span>CHOOSE ACTIVITES <svg width="14" height="8"><path d="M1 1l6 6 6-6" stroke="#fff" fill="none" stroke-width="1.5"/></svg></span>
    </div>
    <span class="btn-teal">BOOK NOW</span>
  </div>
  <div class="dots abs"><i></i><i class="on"></i><i></i></div>
</header>

<section class="features">
  <div class="feat lead" style="left:77px;width:273px;padding-left:66px">uTrundle<small>Gives You :</small></div>
  <div class="feat" style="left:350px;width:261px">
    <svg width="20" height="20" viewBox="0 0 20 20"><path d="M1 9h4v10H1zM7 9l4-8c2 0 3 1 2.5 3L13 7h5c1 0 2 1 1.5 2.5l-2 8c-.3 1-1 1.5-2 1.5H7z" fill="var(--teal)"/></svg>
    The Best Selection</div>
  <div class="feat" style="left:611px;width:261px">
    <svg width="14" height="22" viewBox="0 0 14 22"><text x="7" y="18" font-size="20" font-weight="700" text-anchor="middle" fill="var(--teal)" font-family="Arial">$</text></svg>
    The Lowest Prices</div>
  <div class="feat" style="left:872px;width:251px">
    <svg width="22" height="20" viewBox="0 0 22 20"><path d="M0 1h4l3 11h12l2-8H6" fill="var(--teal)"/><circle cx="9" cy="17" r="2" fill="var(--teal)"/><circle cx="17" cy="17" r="2" fill="var(--teal)"/></svg>
    Fast &amp; Easy Booking</div>
</section>

<section class="dest">
  <h2 class="sec-title abs" style="top:40px">Awesome Destinations</h2>
  <p class="sec-sub abs" style="top:99px">Click to find out more about favorite islands</p>
  <div class="grid abs">
    <div class="tile" role="img" aria-label="Photo of a rocky red cliff above turquoise sea" style="background:linear-gradient(160deg,#2b4a7a 0%,#8a4a2a 40%,#2aa3a8 75%,#0e6b6e 100%)">
      <div class="over">Tenerife<br><svg width="22" height="22" viewBox="0 0 22 22" style="margin-top:8px"><circle cx="9" cy="9" r="7" stroke="#fff" stroke-width="2.5" fill="none"/><path d="M14 14l6 6" stroke="#fff" stroke-width="3"/></svg></div>
    </div>
    <div class="tile" role="img" aria-label="Photo of green mountains under clouds" style="background:linear-gradient(180deg,#6fa3d6 0%,#d9e4ea 35%,#5f8f3a 60%,#2f5a1f 100%)"></div>
    <div class="tile" role="img" aria-label="Photo of a golf course by a lake at sunset" style="background:linear-gradient(180deg,#2c4a6e 0%,#8aa0b8 40%,#6f9a3a 65%,#3f5e2c 100%)"></div>
    <div class="tile" role="img" aria-label="Photo of a rocky shore with red volcanic hill" style="background:linear-gradient(180deg,#3f78c0 0%,#9cc0e6 35%,#9a5a3a 55%,#3a3a3a 100%)"></div>
    <div class="tile" role="img" aria-label="Photo of a sandy beach and deep blue sea" style="background:linear-gradient(180deg,#1a3f8a 0%,#3c74c0 45%,#2a8fb0 62%,#d9b070 80%,#c89a5a 100%)"></div>
    <div class="tile" role="img" aria-label="Photo of a wooden pier over turquoise water" style="background:linear-gradient(180deg,#bcd8e6 0%,#5fc6d0 40%,#1fb0b8 70%,#c8b89a 100%)"></div>
  </div>
  <div class="btn-outline abs" style="top:688px;left:495px;width:207px;height:51px">View All</div>
</section>

<section class="welcome" role="img" aria-label="Photo of mountain bikers on a dirt trail">
  <h2>Welcome To uTrundle</h2>
  <p>After a couple of years of extensive research in which our team of writers, researchers and IT whiz kids have been beavering away incessantly, we are delighted to welcome you to uTrundle, our definitive guide to the Canary Islands and the Madeira Archipelago.</p>
  <span class="get">GET MORE</span>
</section>

<section class="acts">
  <h2 class="sec-title abs" style="top:38px">Popular Activities</h2>
  <p class="sec-sub abs" style="top:97px">Top Things To go in Countries</p>
  <div class="search abs">Search Here <svg width="18" height="18" viewBox="0 0 18 18"><circle cx="7.5" cy="7.5" r="6" stroke="#444" stroke-width="2" fill="none"/><path d="M12 12l5 5" stroke="#444" stroke-width="2.5"/></svg></div>

  <div class="card" style="left:77px">
    <div class="pic" role="img" aria-label="Photo of a golfer on a seaside course" style="background:linear-gradient(180deg,#6fa8d8 0%,#b8d4ea 40%,#4f8a3a 70%,#d8cfa8 100%)"></div>
    <h3>Golf &nbsp;in Gran Canaria</h3>
    <div class="price">$ 145.50</div>
    <p>Lorem ipsum dolor sit amet, consectetur adipiscing elit, sed do.</p>
    <span class="book fill">Book Now</span>
    <div class="foot"><span class="stars">
      <svg width="16" height="15"><path d="M8 0l2.4 5 5.6.6-4.2 3.8 1.2 5.6L8 12.2 3 15l1.2-5.6L0 5.6 5.6 5z" fill="#fff"/></svg><svg width="16" height="15"><path d="M8 0l2.4 5 5.6.6-4.2 3.8 1.2 5.6L8 12.2 3 15l1.2-5.6L0 5.6 5.6 5z" fill="#fff"/></svg><svg width="16" height="15"><path d="M8 0l2.4 5 5.6.6-4.2 3.8 1.2 5.6L8 12.2 3 15l1.2-5.6L0 5.6 5.6 5z" fill="#fff"/></svg><svg width="16" height="15"><path d="M8 0l2.4 5 5.6.6-4.2 3.8 1.2 5.6L8 12.2 3 15l1.2-5.6L0 5.6 5.6 5z" fill="#fff"/></svg><svg width="16" height="15"><path d="M8 0l2.4 5 5.6.6-4.2 3.8 1.2 5.6L8 12.2 3 15l1.2-5.6L0 5.6 5.6 5z" fill="#333"/></svg>
    </span><span>&#128077; Reviews</span></div>
  </div>

  <div class="card" style="left:444px">
    <div class="pic" role="img" aria-label="Photo of a climber on a rock face" style="background:linear-gradient(135deg,#9a9c94 0%,#c8c6bc 45%,#8a8a80 100%)"></div>
    <h3>Climbing &nbsp;in Tenerife</h3>
    <div class="price">$ 270.66</div>
    <p>Lorem ipsum dolor sit amet, consectetur adipiscing elit, sed do.</p>
    <span class="book">Book Now</span>
    <div class="foot"><span class="stars">
      <svg width="16" height="15"><path d="M8 0l2.4 5 5.6.6-4.2 3.8 1.2 5.6L8 12.2 3 15l1.2-5.6L0 5.6 5.6 5z" fill="#fff"/></svg><svg width="16" height="15"><path d="M8 0l2.4 5 5.6.6-4.2 3.8 1.2 5.6L8 12.2 3 15l1.2-5.6L0 5.6 5.6 5z" fill="#fff"/></svg><svg width="16" height="15"><path d="M8 0l2.4 5 5.6.6-4.2 3.8 1.2 5.6L8 12.2 3 15l1.2-5.6L0 5.6 5.6 5z" fill="#fff"/></svg><svg width="16" height="15"><path d="M8 0l2.4 5 5.6.6-4.2 3.8 1.2 5.6L8 12.2 3 15l1.2-5.6L0 5.6 5.6 5z" fill="#333"/></svg><svg width="16" height="15"><path d="M8 0l2.4 5 5.6.6-4.2 3.8 1.2 5.6L8 12.2 3 15l1.2-5.6L0 5.6 5.6 5z" fill="#333"/></svg>
    </span><span>&#128077; Reviews</span></div>
  </div>

  <div class="card" style="left:811px">
    <div class="pic" role="img" aria-label="Photo of a sailor on a sailboat deck" style="background:linear-gradient(180deg,#b8d0e6 0%,#d8e4ee 45%,#5a8ab0 70%,#e8e8e8 100%)"></div>
    <h3>Sailing &nbsp;in La Palma</h3>
    <div class="price">$ 348.05</div>
    <p>Lorem ipsum dolor sit amet, consectetur adipiscing elit, sed do.</p>
    <span class="book">Book Now</span>
    <div class="foot"><span class="stars">
      <svg width="16" height="15"><path d="M8 0l2.4 5 5.6.6-4.2 3.8 1.2 5.6L8 12.2 3 15l1.2-5.6L0 5.6 5.6 5z" fill="#fff"/></svg><svg width="16" height="15"><path d="M8 0l2.4 5 5.6.6-4.2 3.8 1.2 5.6L8 12.2 3 15l1.2-5.6L0 5.6 5.6 5z" fill="#fff"/></svg><svg width="16" height="15"><path d="M8 0l2.4 5 5.6.6-4.2 3.8 1.2 5.6L8 12.2 3 15l1.2-5.6L0 5.6 5.6 5z" fill="#fff"/></svg><svg width="16" height="15"><path d="M8 0l2.4 5 5.6.6-4.2 3.8 1.2 5.6L8 12.2 3 15l1.2-5.6L0 5.6 5.6 5z" fill="#fff"/></svg><svg width="16" height="15"><path d="M8 0l2.4 5 5.6.6-4.2 3.8 1.2 5.6L8 12.2 3 15l1.2-5.6L0 5.6 5.6 5z" fill="#fff"/></svg>
    </span><span>&#128077; Reviews</span></div>
  </div>

  <div class="btn-outline abs" style="top:695px;left:495px;width:207px;height:53px">View All</div>
</section>

<section class="recom" role="img" aria-label="Faded photo of a hiker on a forest trail">
  <h2>Recomonded Tours And Activities</h2>
  <div class="strip abs">
    <div role="img" aria-label="Photo of a scuba diver underwater" style="background:linear-gradient(135deg,#0e2a5a,#1f5fa0)"><span class="label">DIVING</span></div>
    <div role="img" aria-label="Photo of hot air balloons" style="background:linear-gradient(135deg,#5aa0d8,#e0a040 60%,#c84a2a)"></div>
    <div role="img" aria-label="Photo of a surfer in a wave" style="background:linear-gradient(135deg,#1a6fa8,#7fc8e0 50%,#e8f4f8)"></div>
    <div role="img" aria-label="Photo of a climber on a snowy ridge" style="background:linear-gradient(135deg,#6a8ab8,#c8d8e8 50%,#3a5a88)"></div>
    <div role="img" aria-label="Photo of a dune buggy on a dirt track" style="background:linear-gradient(180deg,#8ab8e0,#c8b08a 55%,#8a6a4a)"></div>
    <div role="img" aria-label="Photo of a jet ski on the sea" style="background:linear-gradient(180deg,#2a5a9a,#1a7ab0 60%,#e8eef4)"></div>
  </div>
</section>

<section class="refs">
  <h2>Important Reference, You May Like</h2>
  <ul class="ref-col" style="left:77px"><li>Lorem Ipsume is dummy Text</li><li>Lorem Ipsume is dummy Text</li><li>Lorem Ipsume is dummy Text</li><li>Lorem Ipsume is dummy Text</li></ul>
  <ul class="ref-col" style="left:350px"><li>Lorem Ipsume is dummy Text</li><li>Lorem Ipsume is dummy Text</li><li>Lorem Ipsume is dummy Text</li><li>Lorem Ipsume is dummy Text</li></ul>
  <ul class="ref-col" style="left:620px"><li>Lorem Ipsume is dummy Text</li><li>Lorem Ipsume is dummy Text</li><li>Lorem Ipsume is dummy Text</li><li>Lorem Ipsume is dummy Text</li></ul>
  <ul class="ref-col" style="left:888px"><li>Lorem Ipsume is dummy Text</li><li>Lorem Ipsume is dummy Text</li><li>Lorem Ipsume is dummy Text</li><li>Lorem Ipsume is dummy Text</li></ul>
</section>

<footer class="site-foot">
  <div class="fcol" style="left:80px"><h4>COMPANY</h4><ul><li>About</li><li>uTrundle.net</li><li>Corporate Info</li><li>Site map?</li><li>Blog</li><li>Careers</li></ul></div>
  <div class="fcol" style="left:297px"><h4>SUPPORT</h4><ul><li>Contact us</li><li>FAQs</li><li>Legal</li><li>Privacy Policy</li><li>Legal</li></ul></div>
  <div class="fcol" style="left:495px"><h4>PARTNERSHIPS</h4><ul><li>Supplier sign-up</li><li>Affiliate Programs</li></ul>
    <h4 style="margin-top:14px">LOG – INS</h4><ul><li>Customers</li><li>Suppliers</li><li>Affiliates</li></ul></div>
  <div class="social abs"><i></i><i></i><i></i><i></i><i></i><i></i></div>
  <div class="newsletter abs">Newsletter <svg width="24" height="18" viewBox="0 0 24 18"><rect width="24" height="18" rx="2" fill="var(--teal)"/><path d="M1 2l11 8 11-8" stroke="#0b0b0b" stroke-width="2" fill="none"/></svg></div>
  <div class="copy abs">© <b>uTrundle</b> - 2015. All Rights Reserved.</div>
</footer>

</body>
</html>
```